" Nosso corpo jurídico é constituído por profissionais com vasta experiência na advocacia. A reunião desses profissionais e o amadurecimento de um ideal comum, resultaram na criação de um grupo comprometido com a prestação de serviços jurídicos. Estamos aptos a atender, com eficiência, agilidade e qualidade, atuando em equipe ou individualmente para solução do seu problema, por meio de métodos eficientes e dinâmicos. "

```html
<!DOCTYPE html>
<html lang="pt-BR">
<head>
<meta charset="UTF-8">
<title>Moreira Tavares &amp; Lins — Envelopes</title>
<link rel="stylesheet" href="https://fonts.googleapis.com/css2?family=Cormorant+Garamond:wght@500&family=Lato:wght@400&display=swap">
<style>
  :root {
    --bg: #ecebe8;
    --paper: #ffffff;
    --brown: #3a302c;
    --tan: #c0905e;
    --tan-dark: #a87a4c;
    --ink: #4a403b;
    --muted: #8a817b;
  }
  * { margin: 0; padding: 0; box-sizing: border-box; }
  html, body { width: 1200px; height: 1200px; overflow: hidden; background: var(--bg); }
  .stage { position: relative; width: 1200px; height: 1200px; }

  .envelope { position: absolute; top: 230px; width: 480px; height: 740px; box-shadow: 0 6px 18px rgba(0,0,0,.12); }
  .envelope--front { left: 95px; background: var(--paper); }
  .envelope--back { left: 625px; background: var(--brown); }

  .flap { position: absolute; top: 0; left: 0; width: 100%; height: 90px; }

  .brand { position: absolute; display: flex; align-items: center; gap: 12px; }
  .brand__mark { width: 34px; height: 34px; background: var(--tan); flex: none; }
  .brand__text { display: flex; flex-direction: column; }
  .brand__name {
    font-family: "Cormorant Garamond", serif; font-weight: 500;
    font-size: 22px; line-height: 1.05; letter-spacing: .02em; text-transform: uppercase;
  }
  .brand__tag {
    font-family: "Lato", sans-serif; font-size: 9px; letter-spacing: .35em;
    text-transform: uppercase; margin-top: 5px; color: var(--tan);
  }
  .envelope--front .brand { left: 40px; bottom: 160px; }
  .envelope--front .brand__name { color: var(--ink); }
  .envelope--back .brand { left: 50%; top: 46%; transform: translateX(-50%); }
  .envelope--back .brand__name { color: #f3ece6; }

  .contacts {
    position: absolute; right: 40px; bottom: 42px; list-style: none;
    font-family: "Lato", sans-serif; font-size: 11px; color: var(--muted);
  }
  .contacts li { display: flex; align-items: center; gap: 8px; margin-top: 9px; }
  .contacts svg { width: 12px; height: 12px; flex: none; }

  .base-band { position: absolute; left: 0; bottom: 0; width: 100%; height: 22px; background: var(--tan); }
</style>
</head>
<body>
<main class="stage">

  <section class="envelope envelope--front" aria-label="Envelope, frente">
    <svg class="flap" viewBox="0 0 480 90" preserveAspectRatio="none" aria-hidden="true">
      <polygon points="0,0 480,0 480,60 300,90 0,90" fill="var(--tan)"/>
      <polygon points="0,0 480,0 480,8 0,8" fill="var(--tan-dark)"/>
    </svg>

    <div class="brand">
      <span class="brand__mark"></span>
      <div class="brand__text">
        <span class="brand__name">Moreira Tavares<br>&amp; Lins</span>
        <span class="brand__tag">Advocacia</span>
      </div>
    </div>

    <ul class="contacts">
      <li><svg viewBox="0 0 12 12"><rect x="1" y="2.5" width="10" height="7" fill="none" stroke="var(--tan)"/><path d="M1 3 L6 7 L11 3" fill="none" stroke="var(--tan)"/></svg>contato@mtlins.adv.br</li>
      <li><svg viewBox="0 0 12 12"><circle cx="6" cy="6" r="5" fill="var(--tan)"/></svg>(11) 3000-0000</li>
      <li><svg viewBox="0 0 12 12"><circle cx="6" cy="6" r="5" fill="var(--tan)"/></svg>(11) 90000-0000</li>
      <li><svg viewBox="0 0 12 12"><circle cx="6" cy="6" r="4.5" fill="none" stroke="var(--tan)"/><path d="M1.5 6 H10.5 M6 1.5 V10.5" stroke="var(--tan)"/></svg>www.mtlins.adv.br</li>
      <li><svg viewBox="0 0 12 12"><path d="M6 11 C3 7 2.5 5.5 2.5 4.5 A3.5 3.5 0 0 1 9.5 4.5 C9.5 5.5 9 7 6 11Z" fill="var(--tan)"/></svg>Rua das Palmeiras, 120</li>
    </ul>
  </section>

  <section class="envelope envelope--back" aria-label="Envelope, verso">
    <div class="brand">
      <span class="brand__mark"></span>
      <div class="brand__text">
        <span class="brand__name">Moreira Tavares<br>&amp; Lins</span>
        <span class="brand__tag">Advocacia</span>
      </div>
    </div>
    <div class="base-band"></div>
  </section>

</main>
</body>
</html>
```